Business Card Design Project for International Business Consultanting Firm

KEPT Global was established in 1998 and most recently updated our logo.
We provide advice and consultation regarding international business deals; we are also business brokers; and consultants to entreprenueurs. Excellence across borders is our slogan.

Our Previous business card we had KEPT Global and under that; Business Brokers, Int'l Consultants, Finance, Travel and Tourism. I think we branded ourselves too broad so i will keep within the scope of Business and Finance Brokers Domestic and International.

We are looking for a design that conveys modern elegance with simplicity, and class as well as communicate safety and stability.

Target Market(s)

International and domestic business people, entrepreneurs and professionals

Industry/Entity Type

Safety

Requirements
Must have
• Both sides of the business card must be designed.

Must include our logo which is attached.

I am open to modern sophisticated elegance.

Be extremely creative.

Include an area for name, title, business address, telephone, email address and website address

The look must be polished and clever
Nice to have
• maybe two-tone business card; one side vs the other

```html
<!DOCTYPE html>
<html lang="en">
<head>
<meta charset="utf-8">
<title>KEPT Global – Business Card</title>
<link rel="stylesheet" href="https://fonts.googleapis.com/css2?family=Tinos&family=Arimo:wght@400;700&display=swap">
<style>
  :root {
    --stage: #2b2b2b;
    --brand-blue: #1f6fa8;
    --brand-blue-deep: #17609a;
    --card-white: #f2f3f5;
    --map-tint: #c3cfdc;
    --text-grey: #5a5a5a;
    --text-white: #ffffff;
    --art-light: #e6edf4;
  }
  * { box-sizing: border-box; margin: 0; padding: 0; }
  html, body { width: 1200px; height: 900px; overflow: hidden; }
  body {
    background: var(--stage);
    position: relative;
    font-family: "Arimo", Arial, sans-serif;
  }
  .card {
    position: absolute;
    left: 340px;
    width: 520px;
    height: 297px;
    overflow: hidden;
    box-shadow: 0 10px 30px rgba(0,0,0,.45);
  }

  /* Front side */
  .card--front { top: 110px; background: var(--brand-blue); }
  .front-art {
    position: absolute;
    left: 0; top: 0;
    width: 250px; height: 297px;
    background: linear-gradient(160deg, var(--brand-blue) 0%, var(--art-light) 55%, var(--brand-blue-deep) 100%);
  }
  .front-wordmark {
    position: absolute;
    left: 272px; top: 64px;
    font-family: "Tinos", "Times New Roman", serif;
    color: var(--text-white);
    font-size: 50px;
    line-height: 1;
    font-weight: 400;
  }
  .front-url {
    position: absolute;
    left: 274px; top: 176px;
    color: var(--text-white);
    font-size: 12px;
  }

  /* Back side */
  .card--back { top: 470px; background: var(--card-white); }
  .back-map {
    position: absolute;
    left: 260px; top: 0;
    width: 260px; height: 297px;
    background: linear-gradient(200deg, var(--map-tint) 0%, var(--card-white) 85%);
  }
  .back-logo {
    position: absolute;
    left: 30px; top: 40px;
    display: flex; align-items: center; gap: 10px;
  }
  .back-logo__dot {
    width: 34px; height: 34px; border-radius: 50%;
    background: var(--brand-blue);
  }
  .back-logo__name {
    font-family: "Tinos", "Times New Roman", serif;
    font-size: 28px;
    color: var(--brand-blue);
  }
  .contact {
    position: absolute;
    left: 32px; top: 128px;
    color: var(--text-grey);
    font-size: 13px;
    line-height: 1.4;
  }
  .contact__name { color: var(--brand-blue); font-weight: 700; font-size: 17px; }
  .contact__title { font-size: 12px; margin-bottom: 14px; }
  .contact__address { margin-bottom: 10px; }
  .contact__label { color: var(--brand-blue); }
</style>
</head>
<body>

<section class="card card--front">
  <div class="front-art" role="img" aria-label="World globe illustration showing the Americas"></div>
  <div class="front-wordmark">KEPT<br>Global</div>
  <div class="front-url">www.keptglobal.com</div>
</section>

<section class="card card--back">
  <div class="back-map" role="img" aria-label="Faint map of North and Central America"></div>
  <div class="back-logo">
    <span class="back-logo__dot"></span>
    <span class="back-logo__name">KEPT Global</span>
  </div>
  <div class="contact">
    <p class="contact__name">Daniel Reyes</p>
    <p class="contact__title">Title</p>
    <p class="contact__address">0 Harbor Point Road, Suite 0000, Rivermont 00000 &nbsp;<span class="contact__label">E:</span> daniel@keptglobal.com</p>
    <p><span class="contact__label">T:</span> +123 00 000 5678</p>
    <p><span class="contact__label">W:</span> www.keptglobal.com</p>
  </div>
</section>

</body>
</html>
```